Award winning photographer needs a website.

I need a Plumleaf website that showcases my photos. I want them arranged via category, which might be a specific place or a theme. Here are categories I am thinking of:
1. Yarra Valley and Ranges
2. East coast Tasmania
3. Landscapes
4. Seascapes
5. Urban
6. Nepal
7. Macro
I need to be able to upload and download the photos myself. Currently, there is no need for this site to have an ecommerce component. I would like a blog page where I can post about my photographic adventures and maybe add some short videos of me on my way to the shoot, or of the people I meet. I also want to have it so that each photo has a title and if people click on a photo they can read a story about how I came to shoot it etc. There will also be my contact details and how to purchase a print which will happen through other communications. Like i mentioned, no e commerce at this point. I would like a page for awards as I have several. Here are some URLs of sites I like to give you some idea of what I'm looking at:

https://www.vendrimask.com/
https://tobyfarnellphotography.example/
https://www.maudelinskyphotography.example/

I can upload some images for you to start putting together someting if that hepls

Industry/Entity Type

Photography

Coding

Coded - Design and coding required

Number of Pages Required

5+ page

Font styles to use
Sans Serif

Requirements
Must have
• Multiple pages to display photos in different categories

```html
<!DOCTYPE html>
<html lang="en">
<head>
<meta charset="utf-8">
<title>Adrian Kestrelwood Photography</title>
<link rel="stylesheet" href="https://fonts.googleapis.com/css2?family=Outfit:wght@300;400&display=swap">
<style>
  :root {
    --page-bg: #ffffff;
    --ink: #2b2b2b;
    --muted: #6f7683;
    --rule: #9a9a9a;
    --icon: #8a8a8a;
  }
  * { margin: 0; padding: 0; box-sizing: border-box; }
  html, body { width: 1200px; height: 1020px; overflow: hidden; background: var(--page-bg); }
  body { position: relative; font-family: "Outfit", sans-serif; color: var(--ink); }
  .site-name { position: absolute; top: 28px; left: 0; width: 1200px; text-align: center; font-size: 40px; font-weight: 400; letter-spacing: 0.5px; color: var(--ink); }
  .menu-toggle { position: absolute; left: 1169px; top: 27px; }
  .main-nav a { position: absolute; top: 99px; font-size: 11.5px; letter-spacing: 0.4px; color: var(--ink); text-decoration: none; }
  .main-nav .is-current::after { content: ""; position: absolute; left: -4px; right: -3px; top: 24px; height: 2px; background: var(--rule); }
  .album { position: absolute; }
  .album-cover { display: block; height: 195px; width: 100%; }
  .album-title { position: absolute; left: -1px; top: 216px; font-size: 16px; font-weight: 300; white-space: nowrap; }
  .album-count { position: absolute; left: 0; top: 234px; font-size: 9px; font-weight: 300; letter-spacing: 0.3px; color: var(--muted); white-space: nowrap; }
  .social { position: absolute; top: 957px; left: 547px; display: flex; gap: 14px; }
  .social span { width: 9px; height: 9px; border-radius: 50%; background: var(--icon); }
  .copyright { position: absolute; top: 980px; left: 0; width: 1200px; text-align: center; font-size: 9px; font-weight: 300; }
</style>
</head>
<body>
  <header>
    <div class="site-name">Adrian Kestrelwood</div>
    <svg class="menu-toggle" width="10" height="8" viewBox="0 0 10 8" aria-label="Menu">
      <rect y="0" width="10" height="1.4" fill="#777"/><rect y="3.3" width="10" height="1.4" fill="#777"/><rect y="6.6" width="10" height="1.4" fill="#777"/>
    </svg>
    <nav class="main-nav">
      <a class="is-current" style="left:459px">HOME</a>
      <a style="left:527px">ABOUT</a>
      <a style="left:594px">GALLERY</a>
      <a style="left:672px">CONTACT</a>
    </nav>
  </header>

  <main class="album-grid">
    <article class="album" style="left:134px;top:149px;width:296px">
      <div class="album-cover" role="img" aria-label="Forest creek at golden hour in the Yarra Ranges" style="background:linear-gradient(160deg,#8a7a2a,#4f6220 45%,#9a7a3a 70%,#2f3a14)"></div>
      <h2 class="album-title">Yarra Valley and Ranges</h2><p class="album-count">15 PHOTOS</p>
    </article>
    <article class="album" style="left:453px;top:149px;width:296px">
      <div class="album-cover" role="img" aria-label="Coastal rocks and lone tree under a pink sunset sky" style="background:linear-gradient(180deg,#d8486e,#b83a5e 45%,#5a4a30 65%,#a84a4a)"></div>
      <h2 class="album-title">East Coast Tasmania</h2><p class="album-count">12 PHOTOS</p>
    </article>
    <article class="album" style="left:772px;top:149px;width:296px">
      <div class="album-cover" role="img" aria-label="City skyline at night reflected in a river" style="background:linear-gradient(180deg,#2a2a2e,#4a3a20 55%,#2a2418 75%,#6a5020)"></div>
      <h2 class="album-title">Urban</h2><p class="album-count">12 PHOTOS</p>
    </article>

    <article class="album" style="left:134px;top:409px;width:190px">
      <div class="album-cover" role="img" aria-label="Pink flower close-up on black background" style="background:radial-gradient(circle at 50% 45%,#e0307a 0,#c02060 35%,#000 62%)"></div>
      <h2 class="album-title">Macro</h2><p class="album-count">11 PHOTOS</p>
    </article>
    <article class="album" style="left:348px;top:409px;width:506px">
      <div class="album-cover" role="img" aria-label="Jetty and boathouse at sunset over calm water" style="background:linear-gradient(180deg,#4a4858,#c87a3a 40%,#5a4a48 60%,#3a3a44)"></div>
      <h2 class="album-title">Seascapes</h2><p class="album-count">12 PHOTOS</p>
    </article>
    <article class="album" style="left:877px;top:409px;width:191px">
      <div class="album-cover" role="img" aria-label="Misty mountain valley under dark clouds" style="background:linear-gradient(170deg,#3a3a42,#8a8898 40%,#4a4e52 70%,#1e2018)"></div>
      <h2 class="album-title">Mountains</h2><p class="album-count">11 PHOTOS</p>
    </article>

    <article class="album" style="left:134px;top:669px;width:296px">
      <div class="album-cover" role="img" aria-label="Black and white snowy Himalayan slopes" style="background:linear-gradient(160deg,#5a5a5a,#c8c8c8 45%,#e8e8e8 70%,#3a3a3a)"></div>
      <h2 class="album-title">Nepal</h2><p class="album-count">11 PHOTOS</p>
    </article>
    <article class="album" style="left:453px;top:669px;width:615px">
      <div class="album-cover" role="img" aria-label="Country road through green fields under a stormy sky with a rainbow" style="background:linear-gradient(180deg,#8a7a9a,#c8a8c0 25%,#4a5a80 42%,#3a5a28 60%,#4a5038)"></div>
      <h2 class="album-title">Landscapes</h2><p class="album-count">22 PHOTOS</p>
    </article>
  </main>

  <footer>
    <div class="social" aria-label="Social links"><span></span><span></span><span></span><span></span><span></span></div>
    <p class="copyright">Copyright 2023, Adrian Kestrelwood. All rights reserved</p>
  </footer>
</body>
</html>
```